Red Sea Boat trips in need of Business Card for Private Boat Tours

We need a Business card for a new business set-up in Egypt on the Red Sea for private snorkelling and boat excursions to one of the world's most beautiful reefs. We have wording logo already set-up which matches the boat but we need business cards to be bright and colourful with pictures of boat

Industry/Entity Type

Tourism

Contact Information for Business Card

Two Silver Gulls (font provided) Boat Trips

```html
<!DOCTYPE html>
<html lang="en">
<head>
<meta charset="utf-8">
<title>Two Silver Gulls Boat Trips – Business Card</title>
<link href="https://fonts.googleapis.com/css2?family=Arimo:ital,wght@0,400;0,700;1,700&display=swap" rel="stylesheet">
<style>
  :root {
    --backdrop: #e4e4e4;
    --card-front: #ffffff;
    --ink: #0b2a45;
    --ink-soft: #4a5a68;
    --sea-light: #2ed3d0;
    --sea-mid: #0f8fc4;
    --sea-deep: #0a3f78;
    --sun: #ffb63b;
    --coral: #ff6b4a;
    --logo-light: #ffffff;
  }
  html, body {
    margin: 0;
    width: 1200px;
    height: 1200px;
    overflow: hidden;
    background: var(--backdrop);
    font-family: "Arimo", Arial, sans-serif;
  }
  .canvas { position: relative; width: 1200px; height: 1200px; }
  .card { position: absolute; width: 688px; height: 392px; box-shadow: 0 10px 24px rgba(0,0,0,0.18); overflow: hidden; }
  .card--front { left: 267px; top: 159px; background: var(--card-front); }
  .card--back { left: 262px; top: 653px; }

  .brand { position: absolute; text-align: center; transform: translate(-50%, -50%); white-space: nowrap; }
  .brand__name { font-weight: 700; line-height: 1.1; }
  .brand__tag { font-weight: 700; letter-spacing: 0.3em; text-transform: uppercase; margin-top: 6px; }
  .card--front .brand { left: 190px; top: 192px; }
  .card--front .brand__name { font-size: 32px; color: var(--sea-deep); }
  .card--front .brand__tag { font-size: 14px; color: var(--coral); }
  .card--back .brand { left: 344px; top: 186px; }
  .card--back .brand__name { font-size: 64px; color: var(--logo-light); }
  .card--back .brand__tag { font-size: 22px; color: var(--sun); margin-top: 10px; }

  .divider { position: absolute; left: 366px; top: 72px; width: 2px; height: 236px; background: var(--sea-light); }

  .contact { position: absolute; left: 390px; top: 86px; color: var(--ink-soft); }
  .contact__name { margin: 0; font-size: 26px; font-weight: 700; color: var(--ink); line-height: 1.1; }
  .contact__role { margin: 3px 0 0; font-size: 14px; font-weight: 700; font-style: italic; color: var(--sea-mid); }
  .contact__address { margin: 22px 0 0; font-size: 17px; line-height: 21px; }
  .contact__list { list-style: none; margin: 12px 0 0; padding: 0; font-size: 17px; }
  .contact__list li { display: flex; align-items: center; height: 20.7px; }
  .contact__list svg { width: 14px; height: 14px; margin-right: 12px; fill: var(--sea-mid); flex: none; }

  .footer-rule { position: absolute; left: 0; right: 0; top: 370px; height: 4px; background: var(--sea-light); }
  .footer-band { position: absolute; left: 0; right: 0; bottom: 0; height: 15px; background: linear-gradient(90deg, var(--sea-deep), var(--sea-mid)); }

  .boat-photo {
    position: absolute; inset: 0;
    background: linear-gradient(180deg, var(--sea-light) 0%, var(--sea-mid) 50%, var(--sea-deep) 100%);
  }
</style>
</head>
<body>
<main class="canvas">
  <section class="card card--front" aria-label="Business card front">
    <div class="brand">
      <div class="brand__name">Two Silver Gulls</div>
      <div class="brand__tag">Boat Trips</div>
    </div>
    <div class="divider"></div>
    <div class="contact">
      <h1 class="contact__name">Daniel Hart</h1>
      <p class="contact__role">President</p>
      <p class="contact__address">215 Coral Bay Road<br>Marsa Alam, Egypt 84721</p>
      <ul class="contact__list">
        <li><svg viewBox="0 0 16 16" aria-hidden="true"><path d="M3.6 1.2l2.2 2.6-1.3 1.8c.9 2 2.3 3.5 4.3 4.4l1.8-1.3 2.6 2.2-1 2.6C7 13.2 2.8 9 1.2 3.3z"/></svg>736-555-0142</li>
        <li><svg viewBox="0 0 16 16" aria-hidden="true"><path d="M4.5 1h7v14h-7zM5.8 2.6v9.6h4.4V2.6z" fill-rule="evenodd"/></svg>736-555-0187</li>
        <li><svg viewBox="0 0 16 16" aria-hidden="true"><path d="M1 4h14v9H1zM2.5 5.2L8 9l5.5-3.8v-.1h-11z" fill-rule="evenodd"/></svg>info@twosilvergulls.com</li>
        <li><svg viewBox="0 0 16 16" aria-hidden="true"><circle cx="8" cy="8" r="7"/><path d="M4 5h3v3H5zM9 9h3l-1 3H9z" fill="#fff"/></svg>www.twosilvergulls.com</li>
      </ul>
    </div>
    <div class="footer-rule"></div>
    <div class="footer-band"></div>
  </section>

  <section class="card card--back" aria-label="Business card back">
    <div class="boat-photo" role="img" aria-label="Photo of the tour boat on the turquoise Red Sea over the reef"></div>
    <div class="brand">
      <div class="brand__name">Two Silver Gulls</div>
      <div class="brand__tag">Boat Trips</div>
    </div>
  </section>
</main>
</body>
</html>
```